Guaranteed Job - Sleek Sexy Business Card UV Spot

Im looking for a sleek and sexy business card, that resembles elite or VIP status status.
our business is corinvale.example
you can view our products on there, but our main audience for handing out our cards will be for people in the hospitality industry, so it will need to impress high management and CEO of hotels and restaurants, bars, clubs etc...
the card features will have UV spot on both sides, 400gsm stock. standard size.
Artwork should be 86 x 54mm + 2mm bleed = 90 x 58mm
it should have a nice "unique" uv spot pattern that highlights the card, not a repeated pattern, theres no originality there, and it will be disregarded.
The written material will be:
Corin Vale Hospitality College (logo)
Tobin Marsh
Director
Phone: 1300 615 737
Mobile: 0455 817 296
Email: info@corinvale.example
website: www.corinvale.example
I'm looking for originality here, i don't want just a simple stock card, want something that has a wow factor for people.
You will find the logo attached. you may invert the white to black words to suit the background as you please.
thank you and good luck
As a side note, ive received a lot of proposals, im too busy to give feedback to each and every one, so if i havent provided feedback for your design within 24 hours, then consider it not acceptable, and you could resubmit another design.
So far i have not seen any design that stood out for me, they all seem pretty generic. there nothing thats unique, i would figure for the amount that im offering, that people would put some more effort and creativity into the design.
so far over 200 designs submitted, and nothing i have seen looks very original, everything looks like a different variation of the same stuff, i said it very clearly i wanted something unique, the only thing that has come close to it so far is this one
Reason: Ive received alot of design concepts and i have reviewed everyone, but i havent had time to give feedback to every single one, only the ones that have interested me, if i havent responded, its because i havent found it good enough.
so far only a few design have been on par with what ive been looking for, an attractive eye popping design.
heres a few of them,
http://files.pixelbazaar.example/design_img/51736/62418/62418_2840915_51736_image.jpg
http://files.pixelbazaar.example/design_img/51736/68254/68254_2841377_51736_image.jpg
theyre, both unique and original, and eye catching, the only thing theyre missing is the sexyness.
if you still think you have some creativity left in your minds, then throw it on here.
Reason: Sorry guys for the delay, I was in a serious accident and out of commission for the past few months, I'm just slowly recovering now, please bare with me as i try to attend to this project, it may take me awhile as I have other projects that are on standby, I'm not 100% at the moment, so im extending the deadline for 2 weeks right now. Thanks for your patience.
Hospitality

```html
<!DOCTYPE html>
<html lang="en">
<head>
<meta charset="utf-8">
<title>Corin Vale Hospitality College – Business Card</title>
<link rel="stylesheet" href="https://fonts.googleapis.com/css2?family=Montserrat:wght@400;500;700&family=Cormorant+Garamond:ital,wght@1,400&display=swap">
<style>
  :root {
    --canvas-bg: #555759;
    --card-bg: #050505;
    --text-white: #f2f2f2;
    --brand-blue: #3f97d3;
    --splash-red: #c8203a;
    --splash-magenta: #a0267c;
    --splash-green: #3fae3a;
    --splash-ice: #7fa3b5;
    --splash-orange: #f09a2a;
  }
  * { box-sizing: border-box; margin: 0; padding: 0; }
  html, body {
    width: 1200px;
    height: 900px;
    overflow: hidden;
    background: var(--canvas-bg);
    font-family: "Montserrat", sans-serif;
  }
  .sheet {
    width: 1200px;
    height: 900px;
    display: flex;
    flex-direction: column;
    align-items: center;
    justify-content: center;
    gap: 30px;
  }
  .card {
    position: relative;
    width: 640px;
    height: 402px;
    background: var(--card-bg);
    border-radius: 22px;
    overflow: hidden;
    color: var(--text-white);
  }
  .splash-art {
    position: absolute;
    right: 0;
    top: 0;
    width: 400px;
    height: 402px;
    background:
      radial-gradient(ellipse 30% 22% at 38% 48%, rgba(240,154,42,0.75), transparent 70%),
      radial-gradient(ellipse 34% 34% at 32% 62%, rgba(200,32,58,0.85), transparent 72%),
      radial-gradient(ellipse 30% 30% at 52% 18%, rgba(63,174,58,0.7), transparent 72%),
      radial-gradient(ellipse 32% 48% at 78% 50%, rgba(127,163,181,0.65), transparent 72%),
      radial-gradient(ellipse 40% 30% at 14% 40%, rgba(160,38,124,0.6), transparent 72%);
  }
  .brand {
    position: absolute;
    display: flex;
    align-items: center;
    gap: 12px;
  }
  .brand-mark {
    width: 44px;
    height: 44px;
    background: var(--brand-blue);
    flex: none;
  }
  .brand-name {
    font-weight: 700;
    font-size: 17px;
    line-height: 1.05;
    text-transform: uppercase;
    color: var(--text-white);
    letter-spacing: 0.02em;
    max-width: 150px;
  }
  .card-back .brand { left: 70px; top: 250px; }
  .back-website {
    position: absolute;
    left: 70px;
    top: 318px;
    font-family: "Cormorant Garamond", serif;
    font-style: italic;
    font-size: 26px;
    color: #cfcfcf;
    letter-spacing: 0.04em;
  }
  .card-front .brand { left: 50px; top: 50px; }
  .person {
    position: absolute;
    left: 76px;
    top: 160px;
  }
  .person-name {
    font-size: 24px;
    font-weight: 400;
    color: var(--text-white);
  }
  .person-role {
    font-size: 19px;
    color: var(--brand-blue);
    margin-top: 2px;
  }
  .contact-list {
    position: absolute;
    left: 150px;
    top: 262px;
    list-style: none;
  }
  .contact-item {
    display: flex;
    align-items: center;
    gap: 12px;
    font-size: 15px;
    height: 30px;
    color: var(--text-white);
  }
  .contact-icon {
    width: 16px;
    height: 16px;
    flex: none;
    color: var(--brand-blue);
  }
</style>
</head>
<body>
<main class="sheet">

  <section class="card card-back" aria-label="Card back">
    <div class="splash-art" role="img" aria-label="Cocktail glass with orange slice amid colourful liquid splashes"></div>
    <div class="brand">
      <span class="brand-mark"></span>
      <span class="brand-name">Corin Vale Hospitality College</span>
    </div>
    <p class="back-website">www.corinvale.example</p>
  </section>

  <section class="card card-front" aria-label="Card front">
    <div class="splash-art" role="img" aria-label="Cocktail glass with orange slice amid colourful liquid splashes"></div>
    <div class="brand">
      <span class="brand-mark"></span>
      <span class="brand-name">Corin Vale Hospitality College</span>
    </div>
    <div class="person">
      <p class="person-name">Tobin Marsh</p>
      <p class="person-role">Director</p>
    </div>
    <ul class="contact-list">
      <li class="contact-item">
        <svg class="contact-icon" viewBox="0 0 16 16" aria-hidden="true"><circle cx="8" cy="8" r="7" fill="none" stroke="currentColor" stroke-width="1.4"/><path d="M5.5 4.5c0 3.5 2.5 6.5 5.5 7l.8-1.6-1.8-1-1 .9c-1-.6-1.8-1.6-2.2-2.6l.9-1-1-1.8z" fill="currentColor"/></svg>
        <span>1300 615 737</span>
      </li>
      <li class="contact-item">
        <svg class="contact-icon" viewBox="0 0 16 16" aria-hidden="true"><rect x="4" y="1.5" width="8" height="13" rx="1.5" fill="none" stroke="currentColor" stroke-width="1.4"/><circle cx="8" cy="12" r="0.9" fill="currentColor"/></svg>
        <span>0455 817 296</span>
      </li>
      <li class="contact-item">
        <svg class="contact-icon" viewBox="0 0 16 16" aria-hidden="true"><circle cx="8" cy="8" r="2.6" fill="none" stroke="currentColor" stroke-width="1.4"/><path d="M10.6 5.5v3.3c0 1.6 2.9 1.6 2.9-.8A5.5 5.5 0 1 0 11 12.6" fill="none" stroke="currentColor" stroke-width="1.4"/></svg>
        <span>info@corinvale.example</span>
      </li>
      <li class="contact-item">
        <svg class="contact-icon" viewBox="0 0 16 16" aria-hidden="true"><path d="M8 1.5 1 8h2v6.5h4v-4h2v4h4V8h2z" fill="currentColor"/></svg>
        <span>www.corinvale.example</span>
      </li>
    </ul>
  </section>

</main>
</body>
</html>
```